coaching agenda

Please redesign the brochure attached in a more modern/trendy out look. I want something completely different to what is attached but using the same colours and logo.

```html
<!DOCTYPE html>
<html lang="en">
<head>
<meta charset="utf-8">
<title>Coaching Session Brochure</title>
<link rel="stylesheet" href="https://fonts.googleapis.com/css2?family=Montserrat:wght@500;600;700;800&family=Open+Sans:wght@400;600&display=swap">
<style>
:root{
  --blue:#12a3da;
  --charcoal:#3e3f41;
  --ink:#2b2b2d;
  --muted:#55585c;
  --paper:#ffffff;
  --stage:#dcdcdc;
}
*{margin:0;padding:0;box-sizing:border-box}
html,body{width:1004px;height:1200px;overflow:hidden}
body{background:var(--stage);font-family:"Open Sans",Arial,sans-serif;color:var(--ink);position:relative}
.spread{position:absolute;left:92px;width:820px;height:580px;display:flex;box-shadow:0 4px 14px rgba(0,0,0,.18)}
.spread--outer{top:13px}
.spread--inner{top:607px}
.page{position:relative;width:410px;height:580px;overflow:hidden;background:var(--paper)}

/* back cover */
.back-cover{background:var(--charcoal);color:#fff}
.brand{display:flex;align-items:center;gap:6px;font-family:"Montserrat",sans-serif;font-weight:700}
.brand__square{width:12px;height:12px;background:currentColor;display:block;flex:none}
.brand__name{font-size:13px;letter-spacing:.3px;white-space:nowrap}
.back-cover .brand{position:absolute;left:24px;bottom:32px}
.back-cover .brand__name{font-size:10px}
.contacts{position:absolute;right:16px;bottom:28px;display:flex;gap:14px;font-size:7.5px;line-height:1.5}
.contacts ul{list-style:none}
.contacts li{display:flex;align-items:flex-start;gap:5px;margin-bottom:2px;white-space:nowrap}
.contacts svg{flex:none;margin-top:1px}

/* front cover */
.front-cover svg.cover-shapes{position:absolute;inset:0}
.front-cover .brand{position:absolute;left:40px;top:42px;color:var(--charcoal);flex-direction:column;align-items:flex-start;gap:3px}
.front-cover .brand__row{display:flex;align-items:center;gap:7px}
.front-cover .brand__square{width:14px;height:14px}
.front-cover .brand__name{font-size:17px}
.brand__tag{font-family:"Open Sans",sans-serif;font-weight:400;font-size:7px;color:var(--muted);letter-spacing:.4px}
.cover-title{position:absolute;left:112px;top:340px}
.cover-title__main{display:inline-block;background:var(--blue);color:#fff;font-family:"Montserrat",sans-serif;font-weight:800;font-size:15px;letter-spacing:.6px;padding:5px 12px}
.cover-title__date{display:inline-block;margin-top:6px;background:var(--charcoal);color:#fff;font-family:"Montserrat",sans-serif;font-weight:600;font-size:10px;padding:4px 12px}
.cover-url{position:absolute;left:142px;top:430px;font-size:9px;color:var(--charcoal);font-weight:600}

/* inner pages */
.inner-left{padding:34px 30px 0 34px}
.section-title{font-family:"Montserrat",sans-serif;font-weight:700;color:var(--blue);font-size:14px;margin-bottom:4px}
.question-list{list-style:none;font-size:8px;line-height:1.45;color:var(--muted);margin-bottom:16px}
.lead{font-family:"Montserrat",sans-serif;font-weight:700;font-size:8.5px;color:var(--ink);margin-bottom:5px}
.numbered{list-style:none;font-size:8px;line-height:1.35;color:var(--muted)}
.numbered li{display:flex;gap:10px;margin-bottom:4.5px}
.numbered .num{color:var(--blue);font-weight:600;width:10px;flex:none;font-family:"Montserrat",sans-serif}
.today{position:absolute;left:34px;right:30px;bottom:34px}
.today .lead{font-size:8.5px;line-height:1.4}

.inner-right{padding:34px 0 0 30px}
.intro{width:250px;font-family:"Montserrat",sans-serif;font-weight:700;font-size:8px;line-height:1.35;color:var(--ink);margin-bottom:9px}
.review{width:250px}
.review .numbered li{gap:6px;margin-bottom:4px}
.bullets{display:grid;grid-template-columns:1fr 1fr;column-gap:10px;margin:4px 0 8px 0;font-size:8px;color:var(--muted)}
.bullets ul{list-style:none}
.bullets li{position:relative;padding-left:8px;margin-bottom:5px;line-height:1.3}
.bullets li::before{content:"";position:absolute;left:0;top:4px;width:3px;height:3px;border-radius:50%;background:var(--blue)}
.coach-photo{position:absolute;right:10px;top:48px;width:100px;height:500px;border-radius:45px 45px 8px 8px;background:linear-gradient(180deg,#d7d9dc 0%,#3a4150 35%,#2c3340 100%)}
</style>
</head>
<body>

<section class="spread spread--outer">
  <div class="page back-cover">
    <div class="brand"><span class="brand__square"></span><span class="brand__name">Marcus Hale</span></div>
    <div class="contacts">
      <ul>
        <li><svg width="9" height="9" viewBox="0 0 10 10"><circle cx="5" cy="5" r="5" fill="#12a3da"/><path d="M3.3 2.6l1 1-.5.6a3.6 3.6 0 0 0 2 2l.6-.5 1 1-.6.7c-1.9-.2-3.9-2.2-4.1-4.1z" fill="#fff"/></svg>+30 210 555 0142</li>
        <li><svg width="9" height="9" viewBox="0 0 10 10"><circle cx="5" cy="5" r="5" fill="#12a3da"/><path d="M3.3 2.6l1 1-.5.6a3.6 3.6 0 0 0 2 2l.6-.5 1 1-.6.7c-1.9-.2-3.9-2.2-4.1-4.1z" fill="#fff"/></svg>+30 214 555 0187</li>
        <li><svg width="9" height="9" viewBox="0 0 10 10"><circle cx="5" cy="5" r="5" fill="#12a3da"/><rect x="2.5" y="3.2" width="5" height="3.6" fill="none" stroke="#fff" stroke-width=".8"/><path d="M2.5 3.2L5 5.3 7.5 3.2" fill="none" stroke="#fff" stroke-width=".8"/></svg>info@northbridgeoffice.com</li>
      </ul>
      <ul>
        <li><svg width="9" height="9" viewBox="0 0 10 10"><circle cx="5" cy="5" r="5" fill="#12a3da"/><circle cx="5" cy="5" r="2.4" fill="none" stroke="#fff" stroke-width=".7"/><path d="M2.6 5h4.8M5 2.6v4.8" stroke="#fff" stroke-width=".6"/></svg>www.northbridgeoffice.com</li>
        <li><svg width="9" height="9" viewBox="0 0 10 10"><circle cx="5" cy="5" r="5" fill="#12a3da"/><path d="M5 2.2a2 2 0 0 1 2 2c0 1.5-2 3.6-2 3.6S3 5.7 3 4.2a2 2 0 0 1 2-2z" fill="#fff"/></svg><span>Kerrow Associates | Athens<br>Greece, Lyrion 14-16<br>PO 106 00</span></li>
      </ul>
    </div>
  </div>

  <div class="page front-cover">
    <svg class="cover-shapes" width="410" height="580" viewBox="0 0 410 580">
      <defs>
        <linearGradient id="photoTone" x1="0" y1="0" x2="1" y2="1">
          <stop offset="0" stop-color="#eeeff0"/>
          <stop offset="1" stop-color="#c9cbcd"/>
        </linearGradient>
      </defs>
      <path d="M330 0H410V470C390 470 370 460 360 440L330 380Z" fill="#12a3da"/>
      <path d="M0 0H320A60 60 0 0 1 380 60V340A120 120 0 0 1 260 460H0Z" fill="url(#photoTone)" role="img" aria-label="Black and white photo of the coach mentoring a young agent"/>
      <circle cx="175" cy="365" r="88" fill="#9a9c9f" opacity=".45"/>
    </svg>
    <div class="brand">
      <div class="brand__row"><span class="brand__square"></span><span class="brand__name">Marcus Hale</span></div>
      <span class="brand__tag">Sales Coaching Pty Ltd</span>
    </div>
    <div class="cover-title">
      <span class="cover-title__main">COACHING SESSION</span><br>
      <span class="cover-title__date">JUNE 2018</span>
    </div>
    <div class="cover-url">www.halesalescoach.com</div>
  </div>
</section>

<section class="spread spread--inner">
  <div class="page inner-left">
    <h2 class="section-title">Yesterday – Today – Tomorrow</h2>
    <ul class="question-list">
      <li>How many appraisals/listing presentations are booked in your diary for this week?</li>
      <li>How many appraisals/listing presentations are booked in your diary for next week?</li>
      <li>How many second viewings/private viewings are booked in your diary for this week?</li>
      <li>How many listings will you launch this week?</li>
    </ul>
    <h2 class="section-title">2018/2019 Productivity Gets</h2>
    <p class="lead">There's more to it than numbers:</p>
    <ol class="numbered">
      <li><span class="num">1</span>Increase in market share in your core area</li>
      <li><span class="num">2</span>Increase in commission rates</li>
      <li><span class="num">3</span>Relationships [ data base growth]- future sellers</li>
      <li><span class="num">4</span>Relationships [ data base growth] – buyer prospects</li>
      <li><span class="num">5</span>Number of appointments/appraisals booked each week</li>
      <li><span class="num">6</span>Listing pipeline growth</li>
      <li><span class="num">7</span>Skills development –is an opportunity - you can't be defined as not knowing what to do. Be specific. You can't become a better closer if you don't have people to close on!!</li>
      <li><span class="num">8</span>Managing free time – you can't be defined by time</li>
      <li><span class="num">9</span>Time is an opportunity</li>
      <li><span class="num">10</span>Know your data base system – data base is an opportunity</li>
      <li><span class="num">11</span>Service charter – there is opportunity in service – repeat/referrals/the future seller calls "you in"</li>
      <li><span class="num">12</span>Health &amp; energy leads to better recovery</li>
      <li><span class="num">13</span>Family &amp; self- breaks</li>
      <li><span class="num">14</span>Self-time</li>
      <li><span class="num">15</span>Milestones/benchmarks</li>
      <li><span class="num">16</span>Wealth creation</li>
    </ol>
    <div class="today">
      <h2 class="section-title">Today onwards [12/6/18]</h2>
      <p class="lead">Build the listing pipeline so you have shock coming to market when the sun shines again.</p>
    </div>
  </div>

  <div class="page inner-right">
    <p class="intro">Don't wait until the usual "spring selling session" promo's start to start looking for listings.</p>
    <p class="intro">Get the jump on your competition by having your July to December profile building campaign set in place now &amp; make sure it is fully funded so you don't lose profile momentum.</p>
    <div class="review">
      <ol class="numbered">
        <li><span class="num">1</span>What went well this month?</li>
        <li><span class="num">2</span>Did you convert good days into good weeks, good weeks into a good month?</li>
        <li><span class="num">3</span>How organised were you last week?</li>
        <li><span class="num">4</span>What ideas, actions, processes, systems &amp; motivations have you introduced into your business during the last thirty days?</li>
        <li><span class="num">5</span>What systems do you need to implement to</li>
        <li><span class="num">6</span>create a smoother work flow?</li>
        <li><span class="num">7</span>Are you pursuing what you believe in?</li>
        <li><span class="num">8</span>At what time of the day are you running at</li>
        <li><span class="num">9</span>your true potential?</li>
        <li><span class="num">10</span>What have been your numbers for May?</li>
      </ol>
      <div class="bullets">
        <ul>
          <li>Speak to's</li>
          <li>Appointments</li>
          <li>Appraisals</li>
          <li>Listing presentations</li>
          <li>Listing pipeline</li>
          <li>Listing authorities signed</li>
          <li>Listings launched</li>
          <li>Home opens</li>
        </ul>
        <ul>
          <li>Negotiations</li>
          <li>Sales</li>
          <li>Lessons learned list</li>
          <li>Inroads into the market share in your core area – are you competitive, you when you are being called in.</li>
        </ul>
      </div>
      <ol class="numbered">
        <li><span class="num">11</span>Script session – what was the best script you used last week?</li>
        <li><span class="num">12</span>Stock review</li>
      </ol>
    </div>
    <div class="coach-photo" role="img" aria-label="Full-length cut-out photo of the coach in a dark suit"></div>
  </div>
</section>

</body>
</html>
```